A Maple Syrup Label for a Local Buniness

We are looking for a label for our maple syrup business. Our business currently sells honey, and we are expanding into maple syrup. Our Business name is "Corvale Bees" and we currently have a logo attached below. We would like to incorporate the bee and CB part, but the label could also read "Corvale Farms" with the words maple syrup. We do not want consumers to confuse the maple syrup jars with the honey jars. It should be clear that the jars contain maple syrup. We are open to new designs as well.

```html
<!DOCTYPE html>
<html lang="en">
<head>
<meta charset="utf-8">
<title>Corvale Farms Maple Syrup Label</title>
<link href="https://fonts.googleapis.com/css2?family=Cinzel:wght@400;600&display=swap" rel="stylesheet">
<style>
  :root {
    --backdrop: #efe7dc;
    --label-cream: #f6f3ea;
    --charcoal: #2f2f33;
    --maple-gold: #eab126;
    --banner-white: #f8f6f0;
  }
  html, body {
    margin: 0;
    padding: 0;
    width: 1200px;
    height: 1000px;
    overflow: hidden;
    background: var(--backdrop);
  }
  .label-canvas {
    display: block;
    width: 1200px;
    height: 1000px;
  }
  .label-text {
    font-family: "Cinzel", "Times New Roman", serif;
  }
  .house-name { fill: var(--charcoal); font-size: 44px; font-weight: 600; letter-spacing: 3px; }
  .brand-name { fill: var(--banner-white); font-size: 96px; font-weight: 400; letter-spacing: 2px; }
  .brand-sub { fill: var(--maple-gold); font-size: 60px; font-weight: 400; letter-spacing: 3px; }
  .product-name { fill: var(--charcoal); font-size: 60px; font-weight: 400; letter-spacing: 6px; }
</style>
</head>
<body>
<svg class="label-canvas" viewBox="0 0 1200 1000" xmlns="http://www.w3.org/2000/svg">
  <defs>
    <path id="product-arc" d="M 300 500 A 300 300 0 0 0 900 500"/>
  </defs>

  <g class="label-frame">
    <circle cx="600" cy="500" r="450" fill="var(--label-cream)"/>
    <circle cx="600" cy="500" r="428" fill="none" stroke="var(--charcoal)" stroke-width="12"/>
    <circle cx="600" cy="500" r="406" fill="none" stroke="var(--charcoal)" stroke-width="3"/>
  </g>

  <g class="house-mark">
    <circle cx="392" cy="318" r="16" fill="var(--maple-gold)"/>
    <text class="label-text house-name" x="625" y="334" text-anchor="middle">CORVALE BEES</text>
  </g>

  <g class="name-banner">
    <path d="M 236 398 L 964 398 L 964 568 L 900 568 L 600 658 L 300 568 L 236 568 Z" fill="var(--maple-gold)"/>
    <path d="M 250 408 L 950 408 L 950 558 L 892 558 L 600 645 L 308 558 L 250 558 Z" fill="var(--charcoal)"/>
    <line x1="300" y1="535" x2="440" y2="535" stroke="var(--maple-gold)" stroke-width="4"/>
    <line x1="760" y1="535" x2="900" y2="535" stroke="var(--maple-gold)" stroke-width="4"/>
    <text class="label-text brand-name" x="600" y="498" text-anchor="middle">CORVALE</text>
    <text class="label-text brand-sub" x="600" y="555" text-anchor="middle">FARMS</text>
    <rect x="584" y="580" width="32" height="32" rx="6" fill="var(--maple-gold)" role="img" aria-label="Small maple leaf mark"/>
  </g>

  <text class="label-text product-name">
    <textPath href="#product-arc" startOffset="50%" text-anchor="middle">MAPLE SYRUP</textPath>
  </text>
</svg>
</body>
</html>
```